Website for software company "velbra"

We need a website for our software company/startup named "velbra". We are developing several products (currently 3 standard-software products) which are all in different sectors, but all our products are available for Laptops/PC/Mobile Phones/Tablets, ... We do also create custom software and support our customers with consulting to optimize their processes.
We already have a Logo which you can find in the attached files.
We are a young team of 4 members (two founders and 2 employees).

To get an idea of our products -> the first one is a planning software for healthcare organizations (eg. Mercyway, firebrigade, pharmacy), the second one is a booking software for sport clubs and the third one is a competition software for sports hunting. You see very diverse. Include or ignore this info of our products as you like.

The design has to be a bootstrap 4 (or higher) design. We have licenced FontAwesome as iconset. Responsive design should come without saying.

Coding

Coded - Design and coding required

Number of Pages Required

5+ page

Font styles to use
Sans Serif

Requirements
Must have
• Starting page, product pages, news section, contact, team, services

```html
<!DOCTYPE html>
<html lang="en">
<head>
<meta charset="utf-8">
<title>Velbra Software Company</title>
<link rel="stylesheet" href="https://fonts.googleapis.com/css2?family=Josefin+Sans:wght@400;600;700&family=Lato:wght@400;700&display=swap">
<style>
:root{
  --orange:#f06a25;
  --orange-deep:#e15a17;
  --ink:#1b1b1b;
  --text:#555;
  --muted:#8a8a8a;
  --gray-bg:#eef0f3;
  --white:#fff;
  --dark:#0f0f10;
}
*{box-sizing:border-box;margin:0;padding:0}
html,body{width:1200px;height:4451px;overflow:hidden}
body{position:relative;font-family:'Lato',sans-serif;color:var(--text);background:var(--white)}
.abs{position:absolute}
.heading{font-family:'Josefin Sans',sans-serif;color:var(--ink);font-weight:600}
.label{font-family:'Josefin Sans',sans-serif;color:var(--orange);font-size:14px;font-weight:600;display:flex;align-items:center;gap:8px}
.label::before,.label.center::after{content:"";width:30px;height:1.5px;background:var(--orange)}
.btn{position:absolute;display:flex;align-items:center;justify-content:center;font-family:'Josefin Sans',sans-serif;font-weight:700;font-size:15px;color:var(--white);background:var(--orange)}
.link-more{font-family:'Josefin Sans',sans-serif;font-weight:700;font-size:14px;color:var(--orange)}

/* hero */
.hero-photo{left:0;top:0;width:1200px;height:760px;background:linear-gradient(100deg,#2d3033 0%,#4a4a48 45%,#7a6a5c 70%,#b4a08a 100%)}
.hero-shade{left:0;top:0;width:1200px;height:760px;background:linear-gradient(90deg,rgba(0,0,0,.55),rgba(0,0,0,.1))}
.brand{font-family:'Josefin Sans',sans-serif;font-weight:700;letter-spacing:1px;display:flex;align-items:center;gap:10px}
.brand .mark{width:16px;height:16px;background:var(--orange)}
.nav a{position:absolute;top:54px;font-family:'Josefin Sans',sans-serif;font-size:14px;font-weight:600;color:var(--white);text-decoration:none}
.hero-title{left:110px;top:212px;font-size:62px;line-height:68px;color:var(--white);font-weight:700}
.hero-sub{left:110px;top:438px;padding-left:10px;border-left:3px solid var(--orange);color:var(--white);font-size:14px;font-weight:700}

/* software */
.soft-card{position:absolute;top:1538px;width:281px;height:320px;background:var(--white);border-radius:10px;box-shadow:0 4px 16px rgba(0,0,0,.06);text-align:center}
.soft-card .icon{position:absolute;left:78px;top:-58px;width:124px;height:124px;border-radius:50%;background:var(--orange);border:5px solid #fbd7c3}
.soft-card h3{margin-top:88px;font-size:25px}
.soft-card p{margin:18px 20px 0;font-size:14px;line-height:26px}
.soft-card .link-more{display:block;margin-top:14px}

/* blog */
.blog-card{position:absolute;background:var(--white)}
.photo{position:absolute;background:linear-gradient(135deg,#3c4852,#8c939b)}
.blog-card h4{font-family:'Josefin Sans',sans-serif;font-weight:600;font-size:23px;line-height:29px;color:var(--ink)}
.date{font-size:14px;color:var(--muted);display:flex;align-items:center;gap:8px}
.date::before{content:"";width:12px;height:12px;border-radius:2px;background:var(--orange)}
.blog-card p{font-size:14px;line-height:26px;color:#333}

/* team */
.member{position:absolute;top:2840px;width:234px;height:332px;background:var(--white);box-shadow:0 3px 14px rgba(0,0,0,.07);border-radius:8px;text-align:center;overflow:hidden}
.member .portrait{height:255px;background:linear-gradient(180deg,#dcdcdc,#8f8f8f)}
.member h5{margin-top:16px;font-family:'Josefin Sans',sans-serif;font-weight:700;font-size:18px;color:var(--ink)}
.member span{font-size:14px;color:var(--muted)}

/* contact */
.info-icon{position:absolute;left:175px;width:50px;height:50px;border-radius:50%;background:var(--white);box-shadow:0 3px 10px rgba(0,0,0,.06);display:flex;align-items:center;justify-content:center}
.info h6{font-size:14px;color:var(--ink);font-weight:700}
.info p{font-size:14px;line-height:23px;color:#333}
.field{position:absolute;left:631px;width:348px;border-bottom:1.5px solid #444;font-size:14px;color:#333;padding-bottom:14px}

/* footer */
.foot-col h6{font-family:'Josefin Sans',sans-serif;font-size:18px;font-weight:600;color:var(--white);margin-bottom:18px}
.foot-col a{display:block;color:var(--white);font-size:14px;line-height:30px;text-decoration:none}
</style>
</head>
<body>

<!-- HERO -->
<div class="abs hero-photo" role="img" aria-label="Team walking through a modern open-plan office"></div>
<div class="abs hero-shade"></div>
<div class="abs brand" style="left:130px;top:36px;font-size:48px;color:var(--white)"><span class="mark"></span>VELBRA</div>
<nav class="nav">
  <a style="left:443px;color:var(--orange)">Home</a>
  <a style="left:521px">Our Software</a>
  <a style="left:651px">Our Blog</a>
  <a style="left:748px">About Us</a>
  <a style="left:849px">Contact Us</a>
</nav>
<div class="btn" style="left:970px;top:40px;width:96px;height:42px">Login</div>
<h1 class="abs heading hero-title">Welcome To<br>Velbra Software<br>Company</h1>
<p class="abs hero-sub">Lorem ipsum dolor sit amet, consectetur adipiscing elit, sed</p>
<div class="btn" style="left:110px;top:492px;width:138px;height:46px">Get Started</div>
<div class="btn" style="left:265px;top:492px;width:138px;height:46px;background:transparent;border:1.5px solid var(--white)">Learn More</div>
<svg class="abs" style="left:0;top:630px" width="1200" height="140" viewBox="0 0 1200 140">
  <polygon points="0,12 600,118 1200,12 1200,140 0,140" fill="var(--orange)"/>
  <polygon points="0,20 600,112 1200,20 1200,140 0,140" fill="var(--white)"/>
  <polygon points="300,65 600,112 900,65 600,135" fill="var(--orange)"/>
</svg>

<!-- ABOUT -->
<div class="abs" role="img" aria-label="Woman at work shown inside bold orange geometric blocks" style="left:110px;top:870px;width:455px;height:345px;background:linear-gradient(135deg,#f08a4c,#e26a2a 60%,#2a3a4c)"></div>
<div class="abs label" style="left:597px;top:836px">About Us</div>
<h2 class="abs heading" style="left:597px;top:866px;font-size:34px;line-height:45px">About Velbra Software<br>Company</h2>
<p class="abs" style="left:598px;top:964px;width:492px;font-size:14px;line-height:25.8px;text-align:justify;color:var(--muted)">Lorem ipsum dolor sit amet, consectetur adipiscing elit, sed do eiusmod tempor incididunt ut labore et dolore magna aliqua. Quis ipsum suspendisse ultrices gravida. Risus commodo viverra maecenas accumsan lacus vel facilisis. Lorem ipsum dolor sit amet, consectetur adipiscing elit, sed do eiusmod tempor incididunt ut labore et dolore magna aliqua. Quis ipsum suspendisse ultrices gravida. Risus commodo viverra maecenas accumsan lacus vel facilisis. Lorem ipsum dolor sit amet, consectetur adipiscing elit, sed do eiusmod</p>
<div class="btn" style="left:598px;top:1193px;width:139px;height:47px">Learn More</div>

<!-- SOFTWARE -->
<section class="abs" style="left:0;top:1310px;width:1200px;height:632px;background:var(--gray-bg)">
  <div class="abs label center" style="left:0;width:1200px;top:75px;justify-content:center">Software</div>
  <h2 class="abs heading" style="left:0;width:1200px;top:102px;text-align:center;font-size:34px">Our Software</h2>
</section>
<div class="soft-card" style="left:157px"><div class="icon"></div><h3 class="heading">Healthcare</h3><p>Lorem ipsum dolor sit amet, consectetur adipiscing elit, sed do eiusmod tempor incididunt ut labore et dolore magna aliqua. Quis ipsum suspendisse ultrices</p><span class="link-more">Learn More</span></div>
<div class="soft-card" style="left:459px"><div class="icon"></div><h3 class="heading">Sport Clubs</h3><p>Lorem ipsum dolor sit amet, consectetur adipiscing elit, sed do eiusmod tempor incididunt ut labore et dolore magna aliqua. Quis ipsum suspendisse ultrices</p><span class="link-more">Learn More</span></div>
<div class="soft-card" style="left:761px"><div class="icon"></div><h3 class="heading">Sports Hunting</h3><p>Lorem ipsum dolor sit amet, consectetur adipiscing elit, sed do eiusmod tempor incididunt ut labore et dolore magna aliqua. Quis ipsum suspendisse ultrices</p><span class="link-more">Learn More</span></div>
<svg class="abs" style="left:0;top:0" width="1200" height="1700" viewBox="0 0 1200 1700" aria-hidden="true">
  <g fill="none" stroke="var(--white)" stroke-width="3" stroke-linecap="round" stroke-linejoin="round">
    <path d="M275,1535 l22,-18 l22,18 M285,1530 v18 M309,1530 v18 M268,1550 q29,20 58,0"/>
    <rect x="575" y="1525" width="50" height="28"/><path d="M568,1528 l32,-20 l32,20 M600,1508 v-12 M590,1553 v-12 h20 v12"/>
    <circle cx="903" cy="1540" r="26"/><circle cx="903" cy="1540" r="15"/><circle cx="903" cy="1540" r="5"/><path d="M870,1540 h66 M903,1507 v66"/>
  </g>
</svg>

<!-- BLOG -->
<section class="abs" style="left:0;top:1942px;width:1200px;height:738px;background:linear-gradient(100deg,var(--orange-deep),#f28040 50%,var(--orange-deep))">
  <h2 class="abs heading" style="left:0;width:1200px;top:70px;text-align:center;font-size:34px;color:var(--white)">Our Latest Blog</h2>
</section>
<div class="blog-card" style="left:110px;top:2087px;width:482px;height:517px">
  <div class="photo" role="img" aria-label="Business colleagues reviewing a laptop together" style="left:12px;top:13px;width:460px;height:315px"></div>
  <h4 class="abs" style="left:16px;top:342px">Lorem ipsum dolor sit</h4>
  <div class="abs date" style="left:16px;top:387px">April 16 2022</div>
  <p class="abs" style="left:16px;top:410px;width:440px">Lorem ipsum dolor sit amet, consectetur adipiscing elit, sed do eiusmod tempor incididunt ut labore et dolore</p>
  <span class="abs link-more" style="left:16px;top:477px">Learn More</span>
</div>
<div class="blog-card" style="left:617px;top:2087px;width:471px;height:250px">
  <div class="photo" role="img" aria-label="Developer working on a laptop" style="left:11px;top:13px;width:225px;height:225px"></div>
  <h4 class="abs" style="left:255px;top:20px">Lorem ipsum<br>dolor sit</h4>
  <div class="abs date" style="left:255px;top:90px">April 16 2022</div>
  <p class="abs" style="left:255px;top:112px;width:200px">Lorem ipsum dolor sit amet, consectetur adipiscing elit, sed do eiusmod tempor</p>
  <span class="abs link-more" style="left:255px;top:208px">Learn More</span>
</div>
<div class="blog-card" style="left:617px;top:2357px;width:471px;height:250px">
  <div class="photo" role="img" aria-label="Man typing at a desk in a library office" style="left:11px;top:13px;width:225px;height:225px"></div>
  <h4 class="abs" style="left:255px;top:20px">Lorem ipsum<br>dolor sit</h4>
  <div class="abs date" style="left:255px;top:90px">April 16 2022</div>
  <p class="abs" style="left:255px;top:112px;width:200px">Lorem ipsum dolor sit amet, consectetur adipiscing elit, sed do eiusmod tempor</p>
  <span class="abs link-more" style="left:255px;top:208px">Learn More</span>
</div>

<!-- TEAM -->
<h2 class="abs heading" style="left:0;width:1200px;top:2760px;text-align:center;font-size:34px">Our team</h2>
<div class="member" style="left:112px"><div class="portrait" role="img" aria-label="Portrait of team member"></div><h5>Torin Wexley</h5><span>Lorem Ipsum</span></div>
<div class="member" style="left:359px"><div class="portrait" role="img" aria-label="Portrait of team member with orange overlay" style="background:linear-gradient(180deg,#f28a4e,var(--orange-deep))"></div>
  <div class="abs" style="left:57px;top:112px;display:flex;gap:12px"><span style="width:32px;height:32px;border-radius:50%;background:var(--white)"></span><span style="width:32px;height:32px;border-radius:50%;background:var(--white)"></span><span style="width:32px;height:32px;border-radius:50%;background:var(--white)"></span></div>
  <h5>Maren Holt</h5><span>Lorem Ipsum</span></div>
<div class="member" style="left:606px"><div class="portrait" role="img" aria-label="Portrait of team member"></div><h5>Jasper Quill</h5><span>Lorem Ipsum</span></div>
<div class="member" style="left:853px"><div class="portrait" role="img" aria-label="Portrait of team member"></div><h5>Lysa Brennor</h5><span>Lorem Ipsum</span></div>

<!-- CONTACT -->
<section class="abs" style="left:0;top:3250px;width:1200px;height:830px;background:var(--gray-bg)">
  <div class="abs label center" style="left:0;width:1200px;top:80px;justify-content:center">Contact</div>
  <h2 class="abs heading" style="left:0;width:1200px;top:112px;text-align:center;font-size:34px">Contact Us</h2>
</section>
<div class="info-icon" style="top:3530px"><svg width="16" height="18" viewBox="0 0 16 18"><path d="M8,1 a6,6 0 0 1 6,6 c0,4 -6,10 -6,10 s-6,-6 -6,-10 a6,6 0 0 1 6,-6z" fill="var(--orange)"/><circle cx="8" cy="7" r="2.2" fill="#fff"/></svg></div>
<div class="abs info" style="left:236px;top:3530px;width:300px"><h6>Address</h6><p>Lorem ipsum dolor sit amet, consectetur adipiscing elit</p></div>
<div class="info-icon" style="top:3643px"><svg width="16" height="16" viewBox="0 0 16 16"><path d="M3,1 l3,0 l1,4 l-2,1 a9,9 0 0 0 5,5 l1,-2 l4,1 l0,3 a2,2 0 0 1 -2,2 a13,13 0 0 1 -12,-12 a2,2 0 0 1 2,-2z" fill="var(--orange)"/></svg></div>
<div class="abs info" style="left:236px;top:3643px"><h6>Phone</h6><p>+1 888 888 8888</p></div>
<div class="info-icon" style="top:3740px"><svg width="16" height="12" viewBox="0 0 16 12"><rect width="16" height="12" rx="1" fill="var(--orange)"/><path d="M1,1 l7,5 l7,-5" stroke="#fff" fill="none" stroke-width="1.5"/></svg></div>
<div class="abs info" style="left:236px;top:3740px"><h6>Email</h6><p style="color:var(--orange)">info@velbrasoftware.com</p></div>
<div class="abs" style="left:585px;top:3437px;width:440px;height:445px;background:var(--white)"></div>
<h3 class="abs heading" style="left:631px;top:3478px;font-size:26px">Send Message</h3>
<div class="field" style="top:3540px">Full Name</div>
<div class="field" style="top:3597px">Last Name</div>
<div class="field" style="top:3660px">Address</div>
<div class="field" style="top:3724px">Types Your Message</div>
<div class="btn" style="left:633px;top:3797px;width:110px;height:42px;border-radius:21px">Send</div>

<!-- FOOTER -->
<svg class="abs" style="left:0;top:3955px" width="1200" height="140" viewBox="0 0 1200 140">
  <polygon points="0,135 600,5 1200,135" fill="var(--orange)"/>
  <polygon points="0,140 600,38 1200,140" fill="var(--dark)"/>
</svg>
<footer class="abs" style="left:0;top:4090px;width:1200px;height:361px;background:var(--dark)">
  <div class="abs brand" style="left:110px;top:70px;font-size:60px;color:var(--white)"><span class="mark" style="width:20px;height:20px"></span>VELBRA</div>
  <div class="abs" style="left:208px;top:163px;display:flex;gap:12px"><span style="width:14px;height:14px;border-radius:50%;background:var(--orange)"></span><span style="width:14px;height:14px;border-radius:50%;background:var(--orange)"></span><span style="width:14px;height:14px;border-radius:50%;background:var(--orange)"></span><span style="width:14px;height:14px;border-radius:50%;background:var(--orange)"></span></div>
  <div class="abs foot-col" style="left:490px;top:60px"><h6>Quick Link</h6><a>Home</a><a>Our Software</a><a>Our Blog</a><a>About Us</a><a>Contact Us</a></div>
  <div class="abs foot-col" style="left:644px;top:60px"><h6>Support</h6><a>Terms&amp;condtions</a><a>Privacy Policy</a><a>About Us</a><a>Support</a></div>
  <div class="abs foot-col" style="left:845px;top:60px;width:245px"><h6>Subscribe To Our Newsletter</h6>
    <div style="border-left:2px solid var(--white);border-bottom:1px solid #444;padding:2px 0 8px 12px;font-size:14px;color:#555">Enter Your Email</div>
    <div class="btn" style="position:relative;margin-top:24px;width:120px;height:36px;border-radius:18px">Subscribe</div>
  </div>
  <p class="abs" style="left:0;width:1200px;top:308px;text-align:center;color:var(--white);font-size:14px">©Copyrights 2022 Velbra &nbsp; | &nbsp; All Rights Reserved</p>
</footer>
</body>
</html>
```